Business Card Design

It's an investment advisory service for individuals with all there investment needs. Also financial consulting to businesses and governmental agencies on retirement plans etc. It's personalized not commoditized help. Should show strength, knowledge and money orientation.

Industry/Entity Type

Investment

Contact Information for Business Card

B. Vel R. Financial Consulting and Wealth Management, Mirek Dale Hopstein, 5172 Paseo Las Colinas Verde, San Diego, CA 92084-6617, Registered Investment Advisor

Requirements
Nice to have
• Something money oriented

```html
<!DOCTYPE html>
<html lang="en">
<head>
<meta charset="utf-8">
<title>B. Vel R. Financial Consulting – Business Card</title>
<link rel="stylesheet" href="https://fonts.googleapis.com/css2?family=Exo+2:wght@300;400;600;700&display=swap">
<style>
  :root {
    --page-bg: #e9e6e1;
    --card-light: #ffffff;
    --card-shade: #e4e5e7;
    --brand-blue: #1fa9e6;
    --ink-dark: #2b2b2d;
    --ink-mid: #55585c;
    --stripe-grey: #8e9094;
  }
  * { margin: 0; padding: 0; box-sizing: border-box; }
  html, body {
    width: 1057px; height: 1200px; overflow: hidden;
    background: var(--page-bg);
    font-family: "Exo 2", Arial, sans-serif;
  }
  .card-sheet { position: relative; width: 1057px; height: 1200px; }
  .card {
    position: absolute; top: 215px;
    width: 440px; height: 770px;
    background: radial-gradient(ellipse at 45% 40%, var(--card-light) 0%, #f6f6f7 45%, var(--card-shade) 100%);
    box-shadow: 0 14px 30px rgba(0,0,0,0.22);
  }
  .card--front { left: 58px; }
  .card--back { left: 559px; }

  .firm-name {
    position: absolute;
    display: flex; align-items: flex-start; gap: 12px;
  }
  .firm-name__mark {
    flex: none; width: 14px; height: 14px; margin-top: 7px;
    background: var(--brand-blue);
  }
  .firm-name__text {
    color: var(--ink-mid); font-size: 21px; font-weight: 400;
    line-height: 1.35; letter-spacing: 0.3px;
  }
  .card--front .firm-name { left: 40px; right: 70px; top: 48px; }
  .card--back .firm-name { left: 70px; right: 70px; top: 330px; }
  .card--back .firm-name__text { text-align: left; }

  .side-stripe { position: absolute; right: 20px; width: 26px; }
  .side-stripe--blue { top: 30px; height: 320px; background: var(--brand-blue); }
  .side-stripe--grey { top: 350px; height: 250px; background: var(--stripe-grey); }

  .contact-icons {
    position: absolute; right: 20px; top: 380px; width: 26px;
    display: flex; flex-direction: column; align-items: center; gap: 30px;
  }
  .contact-icons svg { width: 15px; height: 15px; display: block; }

  .holder { position: absolute; right: 60px; top: 292px; text-align: right; }
  .holder__name {
    color: var(--ink-dark); font-size: 28px; font-weight: 700; letter-spacing: 1px;
  }
  .holder__role {
    color: var(--ink-dark); font-size: 12px; font-weight: 600; letter-spacing: 1.5px;
  }

  .contact-list {
    position: absolute; right: 60px; top: 376px; list-style: none; text-align: right;
    color: var(--ink-dark); font-size: 16px; line-height: 45px; letter-spacing: 1px;
  }
  .contact-list li { height: 45px; }

  .address {
    position: absolute; right: 60px; top: 620px; text-align: right;
    font-style: normal;
    color: var(--ink-dark); font-size: 22px; font-weight: 600; line-height: 1.3; letter-spacing: 0.5px;
  }
</style>
</head>
<body>
<main class="card-sheet">
  <section class="card card--front" aria-label="Business card front">
    <div class="firm-name">
      <span class="firm-name__mark" aria-hidden="true"></span>
      <p class="firm-name__text">B. Vel R. Financial Consulting and Wealth Management</p>
    </div>

    <div class="side-stripe side-stripe--blue"></div>
    <div class="side-stripe side-stripe--grey"></div>

    <div class="contact-icons" aria-hidden="true">
      <svg viewBox="0 0 16 16"><path fill="#fff" d="M4 1l2 4-1.5 1.5c.8 2 2.5 3.7 4.5 4.5L10.5 9.5l4 2-1 3c-6 0-12-6-12-12z"/></svg>
      <svg viewBox="0 0 16 16"><rect x="4" y="1" width="8" height="14" rx="1.5" fill="#fff"/><rect x="5.5" y="3" width="5" height="8" fill="#8e9094"/></svg>
      <svg viewBox="0 0 16 16"><rect x="1" y="3" width="14" height="10" fill="#fff"/><path d="M1 3l7 6 7-6" fill="none" stroke="#8e9094" stroke-width="1.3"/></svg>
      <svg viewBox="0 0 16 16"><circle cx="8" cy="8" r="7" fill="#fff"/></svg>
    </div>

    <div class="holder">
      <p class="holder__name">ORLA PENWICK</p>
      <p class="holder__role">GENERAL MANAGER</p>
    </div>

    <ul class="contact-list">
      <li>014 352 7190</li>
      <li>014 352 7190</li>
      <li>orla@bvelr-mail.com</li>
      <li>www.bvelrwealth.com</li>
    </ul>

    <address class="address">
      214 Harbor Row Road<br>
      5th building Street N
    </address>
  </section>

  <section class="card card--back" aria-label="Business card back">
    <div class="firm-name">
      <span class="firm-name__mark" aria-hidden="true"></span>
      <p class="firm-name__text">B. Vel R. Financial Consulting and Wealth Management</p>
    </div>
  </section>
</main>
</body>
</html>
```